Project Management - Web Design Project

Vantrel 4 Management Limited is a company which provides specialist Project Control and Contract Management expertise to the Engineering, Construction and Manufacturing industries. The emphasis is on advanced Project Management techniques in particular Planning & Scheduling, Cost Control, Change Control, Risk Management, Reporting and Contract Administration. We are a global company (albeit a small start-up at this time) and pride ourselves on our ability to support projects to help them achieve their goals and objectives. Our aim is to implement work class control tools in a simple and user friendly manner. We would like the website to appear professional but at the same time easy to navigate and a good balance between text and pictures. The final design should communicate our value added service to our customers, our willingness to support and our structured approach to our work.

Target Market(s)

Project Management professionals working for engineering, construction and manufacturing organisations involved with delivering projects.

Industry/Entity Type

Construction

Requirements
Must have
• The website must include all of the content from the attached Excel brief. The company logo (attached) must also be included in the design. The design must portray a professional look and feel. Please include pictures and photographs related to project management in the engineering, construction and manufacturing industries. We may supplement with pictures of our own during the next steps.
Nice to have
• Emphasis that Vantrel 4 is available to support, guide, direct to achieve positive outcomes for the projects. We work hard at developing our customer relationships. Our employees are experienced in advanced project management techniques.
Should not have
• The design should not use old style fonts. It should look modern and professional. Do not include cartoons or silly illustrations.

```html
<!DOCTYPE html>
<html lang="en">
<head>
<meta charset="utf-8">
<title>Vantrel 4 Management Limited</title>
<link href="https://fonts.googleapis.com/css2?family=Arimo:wght@400;700&display=swap" rel="stylesheet">
<style>
:root{
  --page:#ffffff;
  --ink:#ffffff;
  --social-bg:#141414;
  --nav-top:#2a6fc4;
  --nav-bottom:#0b4a9c;
  --nav-rule:#5f95d6;
  --caption-top:#3a3a3a;
  --caption-bottom:#161616;
  --button-top:#f4f4f4;
  --button-bottom:#bdbdbd;
  --button-ink:#111111;
}
*{margin:0;padding:0;box-sizing:border-box}
html,body{width:1200px;height:2298px;overflow:hidden;background:var(--page);font-family:"Arimo",Arial,sans-serif}
.canvas{position:relative;width:1200px;height:2298px;overflow:hidden}
.hero-backdrop{position:absolute;left:0;top:0;width:1200px;height:840px;
  background:linear-gradient(160deg,#d7d7d7 0%,#f2f2f2 30%,#ffffff 55%,#f4f4f4 100%)}
.social-bar{position:absolute;left:254px;top:0;width:882px;height:119px}
.social-bar svg{position:absolute;inset:0}
.social-links{position:absolute;left:80px;right:20px;top:0;height:119px;display:flex;align-items:center;justify-content:space-around;list-style:none}
.social-links li{color:var(--ink);font-weight:700;font-size:34px}
.main-nav{position:absolute;left:0;top:840px;width:1136px;height:122px;
  background:linear-gradient(var(--nav-top),var(--nav-bottom));display:flex;align-items:center;overflow:hidden}
.main-nav a{color:var(--ink);text-decoration:none;font-size:38px;letter-spacing:1px;white-space:nowrap;position:absolute;top:36px}
.nav-rule{position:absolute;top:0;height:122px;width:3px;background:var(--nav-rule);transform:skewX(-20deg)}
.gallery{position:absolute;left:0;top:967px;width:1136px;height:1267px}
.photo-prev{position:absolute;left:0;top:0;width:187px;height:1267px;
  background:linear-gradient(90deg,#555 0%,#7a7a7a 60%,#3a3a3a 100%)}
.photo-main{position:absolute;left:187px;top:0;width:949px;height:856px;
  background:radial-gradient(circle at 18% 48%,#2a2a2a 0%,#5a5a5a 30%,#8d8d8d 55%,#1d1d1d 100%)}
.arrow-prev{position:absolute;left:21px;top:538px;width:166px;height:161px;background:rgba(235,235,235,.85);border:2px solid #cfcfcf}
.caption{position:absolute;left:187px;top:856px;width:949px;height:411px;
  background:linear-gradient(var(--caption-top),var(--caption-bottom));color:var(--ink);padding:50px 59px}
.caption h2{font-weight:400;font-size:40px;margin-bottom:14px}
.caption p{font-size:37px;line-height:44px;width:820px}
.button{position:absolute;left:59px;top:250px;width:441px;height:110px;border-radius:8px;
  background:linear-gradient(var(--button-top),var(--button-bottom));color:var(--button-ink);
  font-size:40px;display:flex;align-items:center;justify-content:center;gap:26px;text-decoration:none}
</style>
</head>
<body>
<div class="canvas">
  <div class="hero-backdrop" role="img" aria-label="Soft grey abstract light streaks"></div>

  <div class="social-bar">
    <svg width="882" height="119" viewBox="0 0 882 119"><polygon points="60,0 882,0 882,119 0,119" fill="var(--social-bg)"/>
      <g stroke="#555" stroke-width="3"><line x1="270" y1="20" x2="240" y2="100"/><line x1="470" y1="20" x2="440" y2="100"/><line x1="660" y1="20" x2="630" y2="100"/></g></svg>
    <ul class="social-links"><li>Share</li><li>Post</li><li>Network</li><li>Video</li></ul>
  </div>

  <nav class="main-nav">
    <a style="left:-10px">EMENT</a>
    <span class="nav-rule" style="left:220px"></span>
    <a style="left:292px">SPECIALIST SERVICES</a>
    <span class="nav-rule" style="left:790px"></span>
    <a style="left:870px">PROJECTS</a>
  </nav>

  <section class="gallery">
    <div class="photo-prev" role="img" aria-label="Black and white project photograph"></div>
    <a class="arrow-prev" aria-label="Previous slide">
      <svg width="166" height="161" viewBox="0 0 166 161"><polyline points="70,45 105,80 70,115" fill="none" stroke="#777" stroke-width="5"/></svg>
    </a>
    <div class="photo-main" role="img" aria-label="Black and white photo of darts in a dartboard bullseye"></div>
    <div class="caption">
      <h2>LOREM IPSUM</h2>
      <p>Lorem ipsum dolor sit amet, consectetur adipiscing elit.</p>
      <a class="button" href="#">Find out more
        <svg width="18" height="26" viewBox="0 0 18 26"><polyline points="3,3 14,13 3,23" fill="none" stroke="var(--button-ink)" stroke-width="5"/></svg>
      </a>
    </div>
  </section>
</div>
</body>
</html>
```